Sell the dream! Property investment proposal document

We are looking for a proposal document which outlines our vision for property development. The purpose of the document is to raise investment from investors - sell the dream!
Brief summary:
Tarrow Dwellings Developments, is an emerging New Zealand property investment company with a focus on providing unique property investment opportunities.
Our expertise and capabilities in architectural modular homes provide us with a remarkable advantage in tackling the development of properties that are typically considered challenging, remote, or uniquely positioned.
Our specialization in this niche sector of property development not only sets us apart from competitors, but also paves the way for lucrative investment opportunities in the New Zealand property market.
Feel free to use any images from www.tarrowdwellings.co.nz
Target Market(s)
investors for a unique property development opportunity
Industry/Entity Type
luxury property development in unique locations throughout New Zealand
Font styles to use
Colors
Designer to choose only greyscale colors for use in the design.
Look and feel

```html
<!DOCTYPE html>
<html lang="en">
<head>
<meta charset="utf-8">
<title>Tarrow Dwellings Developments – Investment Proposal</title>
<link href="https://fonts.googleapis.com/css2?family=Questrial&family=Montserrat:wght@400;600&display=swap" rel="stylesheet">
<style>
  :root {
    --backdrop: #5a5a5a;
    --ink: #0d0d0d;
    --paper: #ffffff;
    --band: #d9d9d9;
    --muted: #8a8a8a;
    --faint: #2a2a2a;
    --label: #e6e6e6;
  }
  * { box-sizing: border-box; margin: 0; padding: 0; }
  html, body { width: 1200px; height: 2280px; overflow: hidden; background: var(--backdrop); }
  body { position: relative; font-family: "Montserrat", sans-serif; color: var(--ink); }

  .spread { position: absolute; left: 40px; width: 1120px; height: 680px; box-shadow: 0 6px 18px rgba(0,0,0,.45); }
  .spread--cover { top: 60px; }
  .spread--inner-a { top: 820px; }
  .spread--inner-b { top: 1540px; }
  .page-label { position: absolute; top: -24px; font-size: 13px; color: var(--label); font-family: "Montserrat", sans-serif; }

  .page { position: absolute; top: 0; width: 560px; height: 680px; overflow: hidden; }
  .page--left { left: 0; }
  .page--right { left: 560px; }
  .page--dark { background: var(--ink); color: var(--paper); }
  .page--light { background: var(--paper); }

  .photo { position: absolute; }
  .display { font-family: "Questrial", sans-serif; }
  .strip { position: absolute; top: 0; left: 0; right: 0; height: 38px; background: var(--ink); color: var(--paper); display: flex; align-items: center; padding: 0 22px; font-family: "Questrial", sans-serif; }
  .strip--right { justify-content: flex-end; font-size: 22px; letter-spacing: 1px; }
  .strip--left { font-size: 14px; }

  .heading-tab { position: absolute; background: var(--ink); color: var(--paper); font-family: "Questrial", sans-serif; font-size: 34px; line-height: 1.05; padding: 8px 18px; }
  .body-copy { position: absolute; font-size: 11px; line-height: 1.6; }
  .body-copy p + p { margin-top: 10px; }

  .brand-mark { display: flex; align-items: center; gap: 10px; font-family: "Questrial", sans-serif; color: var(--paper); }
  .brand-mark__square { width: 22px; height: 22px; background: var(--paper); }
  .brand-mark__name { font-size: 16px; }
</style>
</head>
<body>

<!-- Cover spread -->
<section class="spread spread--cover">
  <span class="page-label" style="left:60px">Back</span>
  <span class="page-label" style="left:1040px">Front</span>

  <div class="page page--left page--dark">
    <div class="photo" role="img" aria-label="Modern single-storey dark-clad house with pool, wide exterior view"
         style="left:0;top:0;width:560px;height:300px;background:linear-gradient(180deg,#cfd2d3 0%,#9ea3a4 45%,#4a4d4e 75%,#2b2c2c 100%)"></div>
    <svg style="position:absolute;left:0;top:300px" width="560" height="60" viewBox="0 0 560 60">
      <rect width="560" height="60" fill="#d9d9d9"/>
      <polygon points="0,20 440,20 470,50 560,50 560,60 0,60" fill="#0d0d0d"/>
    </svg>
    <div class="display" style="position:absolute;left:20px;top:330px;font-size:150px;color:var(--faint);line-height:1">Tarrow</div>
    <div class="display" style="position:absolute;left:40px;top:420px;font-size:64px;line-height:1">Tarrow</div>
    <div style="position:absolute;left:40px;bottom:40px;font-size:11px;line-height:1.7;color:var(--band)">
      <div>Ph. 09 555 0142</div>
      <div>Web: www.tarrowdwellings.co.nz</div>
    </div>
  </div>

  <div class="page page--right page--dark">
    <div class="photo" role="img" aria-label="Continuation of the house exterior view with lawn and trees"
         style="left:0;top:0;width:560px;height:300px;background:linear-gradient(180deg,#e2e4e4 0%,#a9adad 45%,#555858 75%,#2b2c2c 100%)"></div>
    <div class="strip strip--left" style="justify-content:space-between;background:transparent;color:var(--paper)">
      <span>Sell the dream!</span><span>www.tarrowdwellings.co.nz</span>
    </div>
    <svg style="position:absolute;left:0;top:300px" width="560" height="60" viewBox="0 0 560 60">
      <rect width="560" height="60" fill="#d9d9d9"/>
      <polygon points="0,50 90,50 120,20 560,20 560,60 0,60" fill="#0d0d0d"/>
    </svg>
    <div class="display" style="position:absolute;left:40px;top:390px;font-size:110px;line-height:1">Tarrow</div>
    <div class="display" style="position:absolute;left:80px;top:520px;font-size:28px;letter-spacing:2px;color:var(--band)">Sell the dream!</div>
    <div class="brand-mark" style="position:absolute;left:80px;bottom:40px">
      <span class="brand-mark__square"></span><span class="brand-mark__name">Tarrow Dwellings</span>
    </div>
  </div>
</section>

<!-- Pages 1 and 2 -->
<section class="spread spread--inner-a">
  <span class="page-label" style="left:60px">Page 1</span>
  <span class="page-label" style="left:1040px">Page 2</span>

  <div class="page page--left page--light">
    <div class="strip strip--left" style="justify-content:flex-end">www.tarrowdwellings.co.nz</div>
    <div class="display" style="position:absolute;left:-10px;top:40px;width:90px;height:330px;font-size:84px;color:#e4e4e4;writing-mode:vertical-rl;transform:rotate(180deg);line-height:1">Tarrow</div>
    <div class="heading-tab" style="left:90px;top:58px;right:0">Business Overview</div>
    <div class="body-copy" style="left:110px;top:130px;width:420px">
      <p>Tarrow Dwellings Developments is an emerging New Zealand property investment company focused on unique opportunities in remarkable places.</p>
      <p>Our architectural modular homes let us build where others cannot: remote, challenging and uniquely positioned sites across the country.</p>
      <p>This niche expertise sets us apart and opens the way to rewarding returns for investors who share our vision.</p>
    </div>
    <div class="photo" role="img" aria-label="Bright open-plan living room with sofas and large windows"
         style="left:0;top:340px;width:560px;height:340px;background:linear-gradient(160deg,#f0f0f0 0%,#bdbdbd 50%,#5e5e5e 100%);clip-path:polygon(0 0,85% 0,100% 12%,100% 100%,0 100%)"></div>
  </div>

  <div class="page page--right page--light">
    <div class="strip strip--right">Sell the dream!</div>
    <div class="photo" role="img" aria-label="Bathroom with freestanding bath facing a window onto hills"
         style="left:0;top:38px;width:210px;height:300px;background:linear-gradient(180deg,#d7d7d7 0%,#8f8f8f 60%,#3d3d3d 100%)"></div>
    <div class="body-copy" style="left:225px;top:58px;width:250px">
      <p>Founded by builders and designers who love the land, we began with a single modular home on a steep coastal section.</p>
      <p>Each project since has refined our process, our partners and our standard of finish.</p>
    </div>
    <div class="display" style="position:absolute;right:14px;top:50px;font-size:32px;writing-mode:vertical-rl;line-height:1">Business Origins</div>
    <div class="body-copy" style="left:20px;top:355px;width:200px">
      <p>Our modular method shortens build times, reduces waste and keeps quality consistent in any location.</p>
    </div>
    <div style="position:absolute;left:0;top:460px;width:250px;height:220px;background:var(--ink)">
      <div class="display" style="position:absolute;left:20px;top:20px;font-size:52px;color:var(--paper)">Tarrow</div>
      <div class="brand-mark" style="position:absolute;left:20px;bottom:26px">
        <span class="brand-mark__square"></span><span class="brand-mark__name">Tarrow Dwellings</span>
      </div>
    </div>
    <div class="photo" role="img" aria-label="Modern kitchen with timber ceiling and skylight"
         style="left:250px;top:340px;width:310px;height:340px;background:linear-gradient(200deg,#cfcfcf 0%,#8b8b8b 55%,#3a3a3a 100%)"></div>
  </div>
</section>

<!-- Pages 3 and 4 -->
<section class="spread spread--inner-b">
  <span class="page-label" style="left:60px">Page 3</span>
  <span class="page-label" style="left:1040px">Page 4</span>

  <div class="page page--left page--light">
    <div class="strip strip--left">www.tarrowdwellings.co.nz</div>
    <div class="photo" role="img" aria-label="Interior with floor-to-ceiling windows overlooking mountains and a lake"
         style="left:0;top:38px;width:560px;height:440px;background:linear-gradient(180deg,#e6e6e6 0%,#a8a8a8 40%,#6a6a6a 70%,#333 100%);clip-path:polygon(0 0,100% 0,100% 88%,92% 100%,0 100%)"></div>
    <div class="heading-tab" style="left:0;top:430px;width:330px">Competitive<br>Advantage</div>
    <div class="body-copy" style="left:22px;top:540px;width:510px">
      <p>Homes are crafted off site in a controlled factory, then delivered and assembled on location with minimal disruption.</p>
      <p>Fewer delays and fixed costs give investors clarity from the first day to the final handover.</p>
    </div>
  </div>

  <div class="page page--right page--light">
    <div class="strip strip--right">Sell the dream!</div>
    <div class="heading-tab" style="left:0;top:52px;width:420px;font-size:36px">Financial Summary</div>
    <div class="body-copy" style="left:20px;top:130px;width:520px">
      <p>Each development is modelled with conservative sales values, firm build pricing and clear timelines for investor returns.</p>
      <p>Projected yields, capital structure and exit options are detailed for every site in the schedule that follows.</p>
    </div>
    <div class="photo" role="img" aria-label="Dark modular home at dusk with lit interior and timber deck"
         style="left:150px;top:290px;width:410px;height:390px;background:linear-gradient(180deg,#c9c9c9 0%,#7d7d7d 45%,#2f2f2f 100%);clip-path:polygon(10% 0,100% 0,100% 100%,0 100%,0 8%)"></div>
  </div>
</section>

</body>
</html>
```